Chiropractic Software Company needs Business Cards

We need a bushiness card design for use at a Chiropractic conference. We build billing, practice management, and medical documentation software. Our product is Vantora Chiropractic Software(Vantora for short). On top of our software we have practice success coaches that coordinate with our chiropractor clients to help them grow their practice and treat more patients. Our logo colors are tried-and-true orange-and-blue. We'd like a sterile white background and a clean layout; organizing the following information: Name, Position/Title, Phone Number, Address, email, and our website. On the backside we'd like our Logo and our slogan, "Your Clinic Keel" and our website(http://www.vantorachiropracticsoftware.example)

Industry/Entity Type

Business

```html
<!DOCTYPE html>
<html lang="en">
<head>
<meta charset="utf-8">
<title>Vantora Pty Ltd – Business Cards</title>
<link href="https://fonts.googleapis.com/css2?family=Open+Sans:wght@400;600;700&display=swap" rel="stylesheet">
<style>
  :root {
    --brand-blue: #2f86e6;
    --brand-blue-deep: #1d5fb8;
    --brand-blue-light: #5aa8f2;
    --brand-orange: #f05a1a;
    --ink: #141414;
    --ink-soft: #4a4a4a;
    --paper: #ffffff;
    --backdrop: #f3f3f3;
    --rule: #3a3a3a;
  }
  * { box-sizing: border-box; margin: 0; padding: 0; }
  html, body {
    width: 1200px; height: 1011px; overflow: hidden;
    background: var(--backdrop);
    font-family: "Open Sans", Arial, sans-serif;
  }
  .canvas { position: relative; width: 1200px; height: 1011px; }

  /* ---------- Identity lockup ---------- */
  .lockup {
    position: absolute; left: 170px; top: 110px;
    display: flex; align-items: center; height: 210px;
  }
  .brand-mark { display: flex; align-items: center; gap: 18px; width: 330px; }
  .brand-mark .dot {
    width: 64px; height: 64px; border-radius: 50%; background: var(--brand-orange);
    flex: none;
  }
  .brand-mark .name {
    font-weight: 700; font-size: 46px; letter-spacing: 2px; color: var(--brand-blue);
  }
  .lockup .divider { width: 2px; height: 190px; background: var(--rule); margin: 0 58px 0 30px; }
  .company { line-height: 1; }
  .company .title { color: var(--brand-blue); font-weight: 600; font-size: 66px; letter-spacing: 1px; }
  .company .title small { font-size: 36px; letter-spacing: 1px; margin-left: 6px; }
  .company .slogan { color: var(--ink); font-weight: 600; font-size: 44px; letter-spacing: 1.5px; margin-top: 18px; }

  /* ---------- Cards ---------- */
  .card {
    position: absolute; top: 470px; width: 530px; height: 310px;
    box-shadow: 0 6px 18px rgba(0,0,0,.18);
  }
  .card-back {
    left: 45px;
    background: radial-gradient(ellipse at 50% 35%, var(--brand-blue-light) 0%, var(--brand-blue) 55%, var(--brand-blue-deep) 100%);
    color: var(--paper);
    display: flex; flex-direction: column; align-items: center; justify-content: center;
  }
  .card-back .brand-mark { width: auto; gap: 14px; margin-bottom: 34px; }
  .card-back .brand-mark .dot { width: 46px; height: 46px; }
  .card-back .brand-mark .name { color: var(--paper); font-size: 40px; }
  .card-back .slogan { font-weight: 600; font-size: 17px; }
  .card-back .web { font-weight: 600; font-size: 17px; margin-top: 4px; }

  .card-front { left: 625px; background: var(--paper); }
  .card-front .spine-art {
    position: absolute; left: 0; top: 0; width: 92px; height: 310px;
    background: linear-gradient(90deg, #ffffff 0%, var(--brand-blue-light) 45%, var(--brand-blue-deep) 75%, #ffffff 100%);
  }
  .card-front .header { position: absolute; left: 150px; top: 40px; display: flex; align-items: center; }
  .card-front .brand-mark { width: auto; gap: 8px; }
  .card-front .brand-mark .dot { width: 20px; height: 20px; }
  .card-front .brand-mark .name { font-size: 17px; letter-spacing: 1px; }
  .card-front .header .divider { width: 1px; height: 52px; background: var(--rule); margin: 0 16px; }
  .card-front .company .title { font-size: 22px; }
  .card-front .company .title small { font-size: 13px; margin-left: 3px; }
  .card-front .company .slogan { font-size: 14px; letter-spacing: .5px; margin-top: 3px; }

  .person { position: absolute; left: 158px; top: 142px; }
  .person .full-name { font-weight: 600; font-size: 18px; color: var(--ink-soft); letter-spacing: .5px; }
  .person .role { font-size: 14px; color: var(--ink-soft); }

  .contact { position: absolute; left: 158px; top: 222px; font-size: 13.5px; color: var(--ink-soft); line-height: 1.35; }
  .contact b { color: var(--brand-orange); font-weight: 600; margin-right: 6px; }
  .address { position: absolute; left: 345px; top: 240px; font-size: 13.5px; color: var(--ink-soft); line-height: 1.35; }
  .card-front .web { position: absolute; left: 158px; top: 275px; font-size: 13.5px; color: var(--ink-soft); }
  .card-front .web span { color: var(--brand-blue); }
</style>
</head>
<body>
<main class="canvas">

  <section class="lockup">
    <div class="brand-mark"><span class="dot"></span><span class="name">VANTORA</span></div>
    <div class="divider"></div>
    <div class="company">
      <div class="title">VANTORA<small>PTY LTD</small></div>
      <div class="slogan">YOUR CLINIC KEEL</div>
    </div>
  </section>

  <section class="card card-back">
    <div class="brand-mark"><span class="dot"></span><span class="name">VANTORA</span></div>
    <div class="slogan">Your Clinic Keel</div>
    <div class="web">www.vantorachiropracticsoftware.example</div>
  </section>

  <section class="card card-front">
    <div class="spine-art" role="img" aria-label="Blue illustration of a spinal column running down the left edge"></div>
    <div class="header">
      <div class="brand-mark"><span class="dot"></span><span class="name">VANTORA</span></div>
      <div class="divider"></div>
      <div class="company">
        <div class="title">VANTORA<small>PTY LTD</small></div>
        <div class="slogan">YOUR CLINIC KEEL</div>
      </div>
    </div>
    <div class="person">
      <div class="full-name">DANA WHITLOW</div>
      <div class="role">Chiropractor analist</div>
    </div>
    <div class="contact">
      <div><b>T</b>(03) 5550 1847</div>
      <div><b>E</b>hello@vantora.example</div>
    </div>
    <div class="address">48 Tallow Crest<br>Mt Arden Vic 3999</div>
    <div class="web">www.<span>vantorachiropracticsoftware</span>.example</div>
  </section>

</main>
</body>
</html>
```